Business Card Design

I am a East Coast Florida based company specializing in hauling air conditioning units and Curb adaptors. I would like to see in the design a pickup truck hauling a goose neck trailer and the use of any colors.

Industry/Entity Type

Air Conditioning

Contact Information for Business Card

Pelican Ridge Freight email@ varela4163@mailbrook.com
Dennis (Denny) Varela, Owner. hauling a/c units and curb adapters
Cell 772-555-0147

```html
<!DOCTYPE html>
<html lang="en">
<head>
<meta charset="utf-8">
<title>Pelican Ridge Freight – Business Card</title>
<link rel="stylesheet" href="https://fonts.googleapis.com/css2?family=Oswald:wght@400;500;600;700&display=swap">
<style>
  :root {
    --stage: #1b1b1b;
    --card-white: #ffffff;
    --card-black: #161616;
    --orange: #e0661e;
    --charcoal: #2f2f2f;
    --text-dark: #222222;
    --grey: #9a9a9a;
  }
  * { margin: 0; padding: 0; box-sizing: border-box; }
  html, body { width: 1200px; height: 871px; overflow: hidden; }
  body {
    background: var(--stage);
    font-family: "Oswald", sans-serif;
    position: relative;
  }
  .card {
    position: absolute;
    left: 250px;
    width: 700px;
    height: 400px;
    overflow: hidden;
  }
  /* Back side */
  .card-back {
    top: 24px;
    background: var(--card-black);
  }
  .card-back .brand {
    position: absolute;
    left: 0; right: 0; top: 150px;
    display: flex;
    align-items: center;
    justify-content: center;
    gap: 16px;
  }
  .brand-square {
    width: 34px; height: 34px;
    background: var(--orange);
  }
  .card-back .brand-name {
    color: var(--orange);
    font-weight: 600;
    font-size: 44px;
    letter-spacing: 1px;
  }
  .back-band {
    position: absolute;
    left: 0; right: 0; bottom: 0;
    height: 24px;
    background: var(--orange);
  }
  /* Front side */
  .card-front {
    top: 446px;
    background: var(--card-white);
  }
  .front-brand {
    position: absolute;
    left: 40px; top: 110px;
    width: 250px;
    display: flex;
    align-items: center;
    gap: 12px;
  }
  .front-brand .brand-square { width: 26px; height: 26px; }
  .front-brand .brand-name {
    color: var(--orange);
    font-weight: 600;
    font-size: 28px;
    line-height: 1.05;
  }
  .divider {
    position: absolute;
    left: 304px; top: 52px;
    width: 2px; height: 180px;
    background: var(--orange);
  }
  .contact {
    position: absolute;
    left: 324px; top: 60px;
    right: 20px;
  }
  .contact-name {
    color: var(--orange);
    font-weight: 700;
    font-size: 27px;
    letter-spacing: 0.5px;
  }
  .contact-role {
    color: var(--text-dark);
    font-weight: 500;
    font-size: 16px;
    margin-top: 2px;
  }
  .contact-line {
    display: flex;
    align-items: center;
    gap: 12px;
    color: var(--text-dark);
    font-weight: 500;
    font-size: 21px;
    margin-top: 8px;
  }
  .contact-line svg { flex: none; }
  .vehicle-art {
    position: absolute;
    left: 110px; top: 258px;
    width: 470px; height: 110px;
    border-radius: 8px;
    background: linear-gradient(90deg, #9c2b22 0%, #b5403a 22%, #3a3a3a 38%, #2a2a2a 100%);
    opacity: 0.85;
  }
</style>
</head>
<body>

  <section class="card card-back" aria-label="Business card, back">
    <div class="brand">
      <span class="brand-square"></span>
      <span class="brand-name">Pelican Ridge Freight</span>
    </div>
    <div class="back-band"></div>
  </section>

  <section class="card card-front" aria-label="Business card, front">
    <div class="front-brand">
      <span class="brand-square"></span>
      <span class="brand-name">Pelican Ridge Freight</span>
    </div>
    <div class="divider"></div>
    <div class="contact">
      <p class="contact-name">Dennis (Denny) Varela</p>
      <p class="contact-role">Owner. hauling a/c units and curb, adapters</p>
      <p class="contact-line">
        <svg width="14" height="20" viewBox="0 0 14 20" aria-hidden="true">
          <rect x="1" y="1" width="12" height="18" rx="2" fill="none" stroke="#e0661e" stroke-width="2"/>
          <circle cx="7" cy="15.5" r="1.2" fill="#e0661e"/>
        </svg>
        <span>772-555-0147</span>
      </p>
      <p class="contact-line">
        <svg width="18" height="13" viewBox="0 0 18 13" aria-hidden="true">
          <rect x="0" y="0" width="18" height="13" fill="#e0661e"/>
          <path d="M0 0 L9 7 L18 0" fill="none" stroke="#ffffff" stroke-width="1.5"/>
        </svg>
        <span>varela4163@mailbrook.com</span>
      </p>
    </div>
    <div class="vehicle-art" role="img" aria-label="Red pickup truck towing a black gooseneck flatbed trailer"></div>
  </section>

</body>
</html>
```